PLIVET Buck Slip: Request for Donations to our Program's Development Fund

We would like to create an invitation card/double sided pamplet (about 4x9 inches) to place in orthopaedics clinics and hand/mail out to potential donors about our research program, Westmere Study Group for Joint & Muscle Health. We have attached a copy of a design we've been working with but are looking for more of a professional touch.

Target Market(s)

Patients, Donors

Industry/Entity Type

Medical And Science

Font styles to use
Other font styles liked:
• Gothan Bold, Gotham Book, Gothan, Georgia, Serif, Sans Serif

Colors
ec1f27
f78f20
ffffff
000000
333333
5c5c5c
fbed22
fbee3d
ffc214

Requirements
Must have
• Please use the visual identity standards for guidance to help with colour choice and font selection (https://www.norvalenu.example/brand/system/files/1.0-logo-visual-identity_april2017.pdf)

```html
<!DOCTYPE html>
<html lang="en">
<head>
<meta charset="utf-8">
<title>PLIVET Buck Slip</title>
<link rel="stylesheet" href="https://fonts.googleapis.com/css2?family=Fira+Sans+Condensed:wght@400;600;700&display=swap">
<style>
  :root {
    --white: #ffffff;
    --black: #000000;
    --ink: #555555;
    --ink-soft: #5c5c5c;
    --yellow: #fbed22;
    --gold: #ffc214;
    --orange: #f78f20;
    --red: #ec1f27;
  }
  html, body {
    margin: 0;
    padding: 0;
    overflow: hidden;
    background: var(--white);
  }
  .slip {
    position: relative;
    width: 1200px;
    height: 533px;
    overflow: hidden;
    background: var(--white);
    font-family: "Fira Sans Condensed", "Arial Narrow", sans-serif;
  }
  .slip__art {
    position: absolute;
    inset: 0;
    width: 1200px;
    height: 533px;
  }
  .slip__message {
    position: absolute;
    left: 0;
    right: 0;
    top: 404px;
    margin: 0;
    text-align: center;
    color: var(--ink);
    font-weight: 600;
    font-size: 30px;
    line-height: 33px;
  }
  .slip__band {
    position: absolute;
    left: 0;
    right: 0;
    bottom: 0;
    height: 12px;
    background: linear-gradient(90deg, var(--orange) 0%, var(--gold) 45%, var(--orange) 80%, var(--red) 100%);
  }
  .brand {
    position: absolute;
    right: 12px;
    bottom: 26px;
    display: flex;
    align-items: center;
    gap: 6px;
  }
  .brand__name {
    color: var(--red);
    font-weight: 700;
    font-size: 18px;
    line-height: 1;
    letter-spacing: 0.3px;
  }
  .brand__descriptor {
    color: var(--ink-soft);
    font-weight: 400;
    font-size: 7.5px;
    line-height: 8px;
    width: 92px;
  }
</style>
</head>
<body>
<main class="slip">
  <svg class="slip__art" viewBox="0 0 1200 533" xmlns="http://www.w3.org/2000/svg">
    <defs>
      <linearGradient id="sky" x1="0" y1="0" x2="0" y2="1">
        <stop offset="0" stop-color="#efefef"/>
        <stop offset="1" stop-color="#d2d2d2"/>
      </linearGradient>
      <linearGradient id="swoosh" x1="0" y1="0" x2="1" y2="0.3">
        <stop offset="0" stop-color="#fbee3d"/>
        <stop offset="0.45" stop-color="#ffc214"/>
        <stop offset="1" stop-color="#f78f20"/>
      </linearGradient>
      <radialGradient id="photoTone" cx="0.52" cy="0.5" r="0.6">
        <stop offset="0" stop-color="#3a2a22"/>
        <stop offset="0.22" stop-color="#d9b5a3"/>
        <stop offset="0.55" stop-color="#c9ccd2"/>
        <stop offset="1" stop-color="#eef0f2"/>
      </radialGradient>
    </defs>
    <rect class="art__sky" width="1200" height="533" fill="url(#sky)"/>
    <ellipse class="art__ground" cx="600" cy="620" rx="1000" ry="460" fill="var(--white)"/>
    <ellipse class="art__halo" cx="600" cy="112" rx="545" ry="250" fill="#bcbcbc"/>
    <ellipse class="art__frame" cx="598" cy="95" rx="485" ry="250" fill="var(--black)"/>
    <ellipse class="art__swoosh" cx="595" cy="130" rx="378" ry="251" fill="url(#swoosh)"/>
    <ellipse class="art__photo" cx="602" cy="112" rx="370" ry="214" fill="url(#photoTone)"
             role="img" aria-label="Photo: cupped hands holding dark soil with a small green seedling"/>
  </svg>

  <p class="slip__message">
    Modern medical advances have helped millions of people<br>
    live longer, healthier lives too. We owe these improvements to<br>
    decades of investment in medical research.
  </p>

  <div class="brand">
    <span class="brand__name">PLIVET</span>
    <span class="brand__descriptor">Westmere Study Group for Joint &amp; Muscle Health</span>
  </div>

  <div class="slip__band"></div>
</main>
</body>
</html>
```